Film Production Company Needs HTML Website Design

My production company, VelvetHarborMediaWorks.com , needs to have an HTML design of our website. I would like a minotaur as the company symbol, as well as a hellfire in the background. Something dark and edgy, like we currently have, but different. The password to open the attached zip file is: FBLY7cqu94Obm15HNwYa
Please check out our website and include all of the tabs that are currently in the design, especially the Investor section.

Film Production

```html
<!DOCTYPE html>
<html lang="en">
<head>
<meta charset="utf-8">
<title>Velvet Harbor Media Works</title>
<link rel="stylesheet" href="https://fonts.googleapis.com/css2?family=Almendra+SC&family=Noto+Sans:wght@400&display=swap">
<style>
  :root {
    --page-black: #000000;
    --panel-dark: #0a0605;
    --panel-band: #0d0807;
    --ember: #f26a45;
    --ember-deep: #c2401f;
    --flame-core: #ffb14a;
    --flame-mid: #d9451b;
    --flame-edge: #5a0f05;
    --logo-gold: #f6dfa9;
    --footer-rust: #6e3b27;
    --sound-fill: #8a2d12;
  }
  * { margin: 0; padding: 0; box-sizing: border-box; }
  html, body {
    width: 1200px;
    height: 960px;
    overflow: hidden;
    background: var(--page-black);
  }
  .site {
    position: relative;
    width: 1200px;
    height: 960px;
    background: var(--page-black);
  }
  .site__column {
    position: absolute;
    left: 150px;
    top: 0;
    width: 891px;
    height: 722px;
    background: linear-gradient(180deg, #050302 0%, var(--panel-dark) 70%, rgba(10,6,5,0) 100%);
  }
  .site__band {
    position: absolute;
    left: 150px;
    top: 563px;
    width: 891px;
    height: 160px;
    background: linear-gradient(180deg, var(--panel-band) 0%, rgba(13,8,7,0.6) 70%, rgba(0,0,0,0) 100%);
  }
  .hero-art {
    position: absolute;
    left: 272px;
    top: 40px;
    width: 656px;
    height: 575px;
    background:
      radial-gradient(ellipse 30% 28% at 50% 82%, var(--flame-core) 0%, var(--flame-mid) 45%, rgba(217,69,27,0) 100%),
      radial-gradient(ellipse 34% 50% at 50% 55%, rgba(180,50,18,0.9) 0%, rgba(90,15,5,0.6) 55%, rgba(0,0,0,0) 100%),
      radial-gradient(ellipse 50% 50% at 50% 50%, rgba(90,15,5,0.35) 0%, rgba(0,0,0,0) 100%);
  }
  .brand {
    position: absolute;
    left: 0;
    width: 1200px;
    top: 540px;
    text-align: center;
    font-family: "Almendra SC", serif;
    font-weight: 400;
    color: var(--logo-gold);
  }
  .brand__name {
    display: block;
    font-size: 44px;
    line-height: 48px;
    letter-spacing: 1px;
  }
  .brand__sub {
    display: block;
    font-size: 14px;
    line-height: 16px;
    letter-spacing: 7px;
    margin-top: 2px;
  }
  .main-nav {
    position: absolute;
    top: 614px;
    left: 0;
    width: 1200px;
    height: 24px;
  }
  .main-nav__link {
    position: absolute;
    transform: translateX(-50%);
    font-family: "Almendra SC", serif;
    font-size: 17px;
    line-height: 24px;
    color: var(--ember);
    text-decoration: none;
    white-space: nowrap;
    letter-spacing: 0.5px;
  }
  .site-footer {
    position: absolute;
    top: 663px;
    left: 0;
    width: 1200px;
    text-align: center;
    font-family: "Noto Sans", sans-serif;
    font-size: 10px;
    line-height: 14px;
    color: var(--footer-rust);
  }
  .sound-toggle {
    position: absolute;
    left: 587px;
    top: 685px;
    width: 24px;
    height: 24px;
  }
</style>
</head>
<body>
<div class="site">
  <div class="site__column"></div>
  <div class="site__band"></div>

  <div class="hero-art" role="img" aria-label="Horned minotaur figure standing in hellfire flames with dark thorny branches"></div>

  <div class="brand">
    <span class="brand__name">VELVET HARBOR</span>
    <span class="brand__sub">MEDIA WORKS</span>
  </div>

  <nav class="main-nav">
    <a class="main-nav__link" href="#" style="left:218px">Home</a>
    <a class="main-nav__link" href="#" style="left:348px">About Us</a>
    <a class="main-nav__link" href="#" style="left:475px">News</a>
    <a class="main-nav__link" href="#" style="left:621px">Productions</a>
    <a class="main-nav__link" href="#" style="left:787px">Investors</a>
    <a class="main-nav__link" href="#" style="left:945px">Contact Us</a>
  </nav>

  <footer class="site-footer">VELVET HARBOR MEDIA WORKS © 2014. PRIVACY POLICY</footer>

  <svg class="sound-toggle" viewBox="0 0 24 24" aria-label="Sound toggle" role="img">
    <circle cx="12" cy="12" r="11" fill="var(--sound-fill)"/>
    <path d="M6 10h3l4-3v10l-4-3H6z" fill="#1a0703"/>
    <path d="M15 9.5q2 2.5 0 5" stroke="#1a0703" stroke-width="1.3" fill="none"/>
  </svg>
</div>
</body>
</html>
```